Ramadan calander & epos strip for retail shop

Ramadan Calendar showcasing our special offers instore as well as informing of prayer times. Should be vibrant, elegant and something you would keep for a month. Please use the design attached for 2019 as your base we like this design and improve upon it but please use last years 2023 calender for all formating and text . Colours have to be green and gold. We also need a shelf edge strip matching with design measuring 1000mm x 40mm.

Target Market(s)

SHOP

Industry/Entity Type

Retail

Font styles to use
Decorative

Colors
00AB8E
00BBA5
67D7C9
C6EFE9
E9F9F6

Requirements
Must have
• Timetable with prayers, 4 product offers on front page, 12 product offers on rear. Logon on the front and back page. Only can use green and gold. ( different shades are acceptable)
Nice to have
• Islamic art, please use 2019 design as a guide
Should not have
• stick to brief

```html
<!DOCTYPE html>
<html lang="en">
<head>
<meta charset="utf-8">
<title>Zahra Market – Ramadan Calendar &amp; Shelf Strip</title>
<link href="https://fonts.googleapis.com/css2?family=Cinzel:wght@700&family=Great+Vibes&family=Oswald:wght@500;700&family=Roboto+Condensed:wght@400;700&display=swap" rel="stylesheet">
<style>
  :root{
    --bg:#eeeeee;
    --green-deep:#173d14;
    --green:#2c5a1d;
    --green-mid:#3f7328;
    --green-light:#5d8f3a;
    --gold:#d4a93a;
    --gold-light:#f0d46a;
    --gold-pale:#f7e9b0;
    --ink:#1b2a12;
    --white:#ffffff;
  }
  *{box-sizing:border-box;margin:0;padding:0}
  html,body{width:1200px;height:3000px;overflow:hidden;background:var(--bg)}
  body{font-family:"Roboto Condensed",Arial,sans-serif;color:var(--white);position:relative}

  .brand{font-family:"Cinzel",Georgia,serif;font-weight:700;color:var(--gold);letter-spacing:4px;display:flex;align-items:center;gap:10px}
  .brand .dot{width:14px;height:14px;border-radius:50%;background:var(--gold)}
  .script{font-family:"Great Vibes",cursive;color:var(--gold-light);line-height:1}

  /* shelf strip */
  .shelf-strip{position:absolute;left:40px;top:40px;width:1120px;height:45px;
    background:linear-gradient(180deg,var(--green-mid),var(--green-deep));
    border-top:3px solid var(--gold);border-bottom:3px solid var(--gold);
    display:flex;align-items:center;justify-content:space-between;padding:0 18px}
  .shelf-strip .brand{font-size:20px}
  .shelf-strip .script{font-size:28px}
  .strip-pattern{width:380px;height:26px;border-radius:3px;
    background:linear-gradient(90deg,rgba(212,169,58,.15),rgba(212,169,58,.45),rgba(212,169,58,.15))}

  /* pages */
  .page{position:absolute;left:100px;width:1000px;height:1390px;overflow:hidden;
    background:radial-gradient(ellipse at 50% 35%,var(--green-light) 0%,var(--green) 45%,var(--green-deep) 100%);
    box-shadow:0 6px 20px rgba(0,0,0,.25)}
  .page-front{top:125px}
  .page-back{top:1555px}

  .page-header{position:absolute;left:0;top:0;width:100%;height:190px;padding:34px 44px}
  .page-header .brand{font-size:52px}
  .tagline{font-size:15px;letter-spacing:6px;color:var(--gold-pale);margin-top:4px;padding-left:26px}
  .lanterns{position:absolute;right:60px;top:0;width:300px;height:170px;
    background:linear-gradient(180deg,rgba(240,212,106,.55),rgba(212,169,58,.1))}
  .page-front .script.heading{position:absolute;left:48px;top:128px;font-size:44px}

  /* offer cards */
  .offer-grid{position:absolute;left:44px;top:200px;width:912px;display:grid;
    grid-template-columns:1fr 1fr;gap:16px 40px}
  .offer{height:160px;display:flex;align-items:center;gap:22px}
  .product{width:200px;height:150px;border-radius:10px;
    background:linear-gradient(160deg,rgba(255,255,255,.35),rgba(212,169,58,.25))}
  .price{width:150px;height:150px;border-radius:50%;background:var(--green-deep);
    border:5px solid var(--gold);display:flex;flex-direction:column;align-items:center;justify-content:center;
    font-family:"Oswald",Arial,sans-serif;color:var(--white)}
  .price .qty{font-size:22px;font-weight:500;color:var(--gold-light);line-height:1}
  .price .amount{font-size:44px;font-weight:700;line-height:1.05}

  .notice{position:absolute;left:44px;top:1100px;width:912px;height:52px;background:var(--gold-light);
    color:var(--ink);font-weight:700;font-size:20px;display:flex;align-items:center;justify-content:center;
    border-radius:4px;letter-spacing:.5px}
  .skyline{position:absolute;left:0;bottom:0;width:100%;height:220px;
    background:linear-gradient(180deg,rgba(212,169,58,0),rgba(212,169,58,.55))}

  /* back page */
  .page-back .page-header{height:150px}
  .flag{position:absolute;right:50px;top:44px;width:96px;height:60px;background:var(--gold-pale);border:2px solid var(--gold)}
  .timetable{position:absolute;left:36px;top:150px;width:640px;border-collapse:collapse;font-size:16px}
  .timetable th{background:var(--gold);color:var(--ink);font-weight:700;padding:8px 4px;font-size:15px}
  .timetable td{padding:0 4px;height:30px;text-align:center;color:var(--white);border-bottom:1px solid rgba(212,169,58,.35)}
  .timetable tr:nth-child(even) td{background:rgba(0,0,0,.15)}
  .timetable tr.odd-night td{background:var(--gold-light);color:var(--ink);font-weight:700}
  .side-offers{position:absolute;right:36px;top:150px;width:270px;display:flex;flex-direction:column;gap:14px}
  .side-offers .offer{height:150px;gap:10px}
  .side-offers .product{width:120px;height:140px}
  .side-offers .price{width:138px;height:138px}
  .side-offers .price .amount{font-size:38px}
  .open-note{position:absolute;right:36px;top:830px;width:270px;text-align:center;font-family:"Oswald",Arial,sans-serif;
    font-size:20px;color:var(--gold-pale);letter-spacing:1px;line-height:1.3}
  .page-back .script.heading{position:absolute;right:36px;top:920px;width:270px;text-align:center;font-size:58px}
  .year{font-family:"Cinzel",Georgia,serif;font-size:34px;color:var(--gold);display:block;margin-top:6px}
</style>
</head>
<body>

<div class="shelf-strip">
  <div class="brand"><span class="dot"></span>ZAHRA MARKET</div>
  <div class="strip-pattern" role="img" aria-label="Gold Islamic geometric border pattern"></div>
  <div class="script">Ramadan Kareem 2025</div>
</div>

<section class="page page-front">
  <header class="page-header">
    <div class="brand"><span class="dot"></span>ZAHRA MARKET</div>
    <div class="tagline">FOOD &amp; GROCERY</div>
    <div class="lanterns" role="img" aria-label="Hanging gold Ramadan lanterns"></div>
    <div class="script heading">Ramadan Kareem 2025</div>
  </header>

  <div class="offer-grid">
    <div class="offer"><div class="product" role="img" aria-label="Product photo: dates pack"></div><div class="price"><span class="qty">2 for</span><span class="amount">£3</span></div></div>
    <div class="offer"><div class="product" role="img" aria-label="Product photo: juice bottle"></div><div class="price"><span class="amount">£2.49</span></div></div>
    <div class="offer"><div class="product" role="img" aria-label="Product photo: canned drinks"></div><div class="price"><span class="qty">2 for</span><span class="amount">£1.50</span></div></div>
    <div class="offer"><div class="product" role="img" aria-label="Product photo: yoghurt tub"></div><div class="price"><span class="amount">£3.25</span></div></div>
    <div class="offer"><div class="product" role="img" aria-label="Product photo: rice sack"></div><div class="price"><span class="amount">£19.99</span></div></div>
    <div class="offer"><div class="product" role="img" aria-label="Product photo: cooking oil"></div><div class="price"><span class="qty">2 for</span><span class="amount">£4.00</span></div></div>
    <div class="offer"><div class="product" role="img" aria-label="Product photo: tea box"></div><div class="price"><span class="qty">2 for</span><span class="amount">£7.00</span></div></div>
    <div class="offer"><div class="product" role="img" aria-label="Product photo: spice packet"></div><div class="price"><span class="amount">£1.00</span></div></div>
    <div class="offer"><div class="product" role="img" aria-label="Product photo: flour bag"></div><div class="price"><span class="amount">£5.99</span></div></div>
    <div class="offer"><div class="product" role="img" aria-label="Product photo: samosa pastry"></div><div class="price"><span class="qty">2 for</span><span class="amount">£2.50</span></div></div>
  </div>

  <div class="notice">PLEASE REMEMBER TO CALCULATE YOUR ZAKAT &amp; FITRANA BEFORE EID PRAYER</div>
  <div class="skyline" role="img" aria-label="Gold mosque skyline silhouette"></div>
</section>

<section class="page page-back">
  <header class="page-header">
    <div class="brand"><span class="dot"></span>ZAHRA MARKET</div>
    <div class="tagline">FOOD &amp; GROCERY</div>
    <div class="flag" role="img" aria-label="National flag"></div>
  </header>

  <table class="timetable">
    <thead><tr><th>Roza</th><th>Day</th><th>Date</th><th>Sehri</th><th>Sunrise</th><th>Zuhr</th><th>Asr</th><th>Iftar</th><th>Isha</th></tr></thead>
    <tbody>
      <tr><td>1</td><td>Sat</td><td>1 Mar</td><td>5:05</td><td>6:50</td><td>12:19</td><td>3:35</td><td>5:45</td><td>7:15</td></tr>
      <tr><td>2</td><td>Sun</td><td>2 Mar</td><td>5:03</td><td>6:48</td><td>12:19</td><td>3:36</td><td>5:47</td><td>7:17</td></tr>
      <tr><td>3</td><td>Mon</td><td>3 Mar</td><td>5:01</td><td>6:46</td><td>12:19</td><td>3:37</td><td>5:49</td><td>7:19</td></tr>
      <tr><td>4</td><td>Tue</td><td>4 Mar</td><td>4:59</td><td>6:44</td><td>12:19</td><td>3:38</td><td>5:51</td><td>7:21</td></tr>
      <tr><td>5</td><td>Wed</td><td>5 Mar</td><td>4:57</td><td>6:42</td><td>12:19</td><td>3:39</td><td>5:53</td><td>7:23</td></tr>
      <tr><td>6</td><td>Thu</td><td>6 Mar</td><td>4:55</td><td>6:40</td><td>12:18</td><td>3:40</td><td>5:55</td><td>7:25</td></tr>
      <tr><td>7</td><td>Fri</td><td>7 Mar</td><td>4:53</td><td>6:38</td><td>12:18</td><td>3:41</td><td>5:57</td><td>7:27</td></tr>
      <tr><td>8</td><td>Sat</td><td>8 Mar</td><td>4:51</td><td>6:36</td><td>12:18</td><td>3:42</td><td>5:59</td><td>7:29</td></tr>
      <tr><td>9</td><td>Sun</td><td>9 Mar</td><td>4:49</td><td>6:34</td><td>12:18</td><td>3:43</td><td>6:01</td><td>7:31</td></tr>
      <tr><td>10</td><td>Mon</td><td>10 Mar</td><td>4:47</td><td>6:32</td><td>12:17</td><td>3:44</td><td>6:03</td><td>7:33</td></tr>
      <tr><td>11</td><td>Tue</td><td>11 Mar</td><td>4:45</td><td>6:30</td><td>12:17</td><td>3:45</td><td>6:05</td><td>7:35</td></tr>
      <tr><td>12</td><td>Wed</td><td>12 Mar</td><td>4:43</td><td>6:28</td><td>12:17</td><td>3:46</td><td>6:07</td><td>7:37</td></tr>
      <tr><td>13</td><td>Thu</td><td>13 Mar</td><td>4:41</td><td>6:26</td><td>12:16</td><td>3:47</td><td>6:09</td><td>7:39</td></tr>
      <tr><td>14</td><td>Fri</td><td>14 Mar</td><td>4:39</td><td>6:24</td><td>12:16</td><td>3:48</td><td>6:11</td><td>7:41</td></tr>
      <tr><td>15</td><td>Sat</td><td>15 Mar</td><td>4:37</td><td>6:22</td><td>12:16</td><td>3:49</td><td>6:13</td><td>7:43</td></tr>
      <tr><td>16</td><td>Sun</td><td>16 Mar</td><td>4:35</td><td>6:20</td><td>12:15</td><td>3:50</td><td>6:15</td><td>7:45</td></tr>
      <tr><td>17</td><td>Mon</td><td>17 Mar</td><td>4:33</td><td>6:18</td><td>12:15</td><td>3:51</td><td>6:17</td><td>7:47</td></tr>
      <tr><td>18</td><td>Tue</td><td>18 Mar</td><td>4:31</td><td>6:16</td><td>12:15</td><td>3:52</td><td>6:19</td><td>7:49</td></tr>
      <tr><td>19</td><td>Wed</td><td>19 Mar</td><td>4:29</td><td>6:14</td><td>12:14</td><td>3:53</td><td>6:21</td><td>7:51</td></tr>
      <tr><td>20</td><td>Thu</td><td>20 Mar</td><td>4:27</td><td>6:12</td><td>12:14</td><td>3:54</td><td>6:23</td><td>7:53</td></tr>
      <tr class="odd-night"><td>21</td><td>Fri</td><td>21 Mar</td><td>4:25</td><td>6:10</td><td>12:14</td><td>3:55</td><td>6:25</td><td>7:55</td></tr>
      <tr><td>22</td><td>Sat</td><td>22 Mar</td><td>4:23</td><td>6:08</td><td>12:13</td><td>3:56</td><td>6:27</td><td>7:57</td></tr>
      <tr class="odd-night"><td>23</td><td>Sun</td><td>23 Mar</td><td>4:21</td><td>6:06</td><td>12:13</td><td>3:57</td><td>6:29</td><td>7:59</td></tr>
      <tr><td>24</td><td>Mon</td><td>24 Mar</td><td>4:19</td><td>6:04</td><td>12:13</td><td>3:58</td><td>6:31</td><td>8:01</td></tr>
      <tr class="odd-night"><td>25</td><td>Tue</td><td>25 Mar</td><td>4:17</td><td>6:02</td><td>12:12</td><td>3:59</td><td>6:33</td><td>8:03</td></tr>
      <tr><td>26</td><td>Wed</td><td>26 Mar</td><td>4:15</td><td>6:00</td><td>12:12</td><td>4:00</td><td>6:35</td><td>8:05</td></tr>
      <tr class="odd-night"><td>27</td><td>Thu</td><td>27 Mar</td><td>4:13</td><td>5:58</td><td>12:12</td><td>4:01</td><td>6:37</td><td>8:07</td></tr>
      <tr><td>28</td><td>Fri</td><td>28 Mar</td><td>4:11</td><td>5:56</td><td>12:11</td><td>4:02</td><td>6:39</td><td>8:09</td></tr>
      <tr class="odd-night"><td>29</td><td>Sat</td><td>29 Mar</td><td>4:09</td><td>5:54</td><td>12:11</td><td>4:03</td><td>6:41</td><td>8:11</td></tr>
      <tr><td>30</td><td>Sun</td><td>30 Mar</td><td>4:07</td><td>5:52</td><td>12:11</td><td>4:04</td><td>6:43</td><td>8:13</td></tr>
    </tbody>
  </table>

  <div class="side-offers">
    <div class="offer"><div class="product" role="img" aria-label="Product photo: milk carton"></div><div class="price"><span class="qty">2 for</span><span class="amount">£7.49</span></div></div>
    <div class="offer"><div class="product" role="img" aria-label="Product photo: bread loaf"></div><div class="price"><span class="qty">2 for</span><span class="amount">£1.50</span></div></div>
    <div class="offer"><div class="product" role="img" aria-label="Product photo: chickpea tins"></div><div class="price"><span class="qty">2 for</span><span class="amount">£4.00</span></div></div>
    <div class="offer"><div class="product" role="img" aria-label="Product photo: honey jar"></div><div class="price"><span class="amount">£3.79</span></div></div>
  </div>

  <div class="open-note">WE'RE OPEN LATE<br>VISIT IN STORE FOR MORE OFFERS</div>
  <div class="script heading">Ramadan Kareem<span class="year">2025</span></div>

  <div class="skyline" role="img" aria-label="Gold mosque skyline silhouette"></div>
</section>

</body>
</html>
```